Life Coaching business needs a new flyer

We are an Australian business that specialises in Life Coaching, Career Coaching, Health and Wellness Coaching, Yoga and Pilates. We need a A4 double sided flyer that is full colour and folded to DL format. I have attached a couple of designs that I like and some pictures and would like the flyer to be bright yet stylish.

Life Coaching

```html
<!DOCTYPE html>
<html lang="en">
<head>
<meta charset="utf-8">
<title>Clearpath Coaching – DL Flyer</title>
<link href="https://fonts.googleapis.com/css2?family=Arimo:ital,wght@0,400;0,700;1,700&family=Roboto+Condensed:wght@400;700&display=swap" rel="stylesheet">
<style>
  :root{
    --page:#eeeeee;
    --paper:#ffffff;
    --green:#4fae3c;
    --blue:#3f8fd6;
    --brand-blue:#1f7fc4;
    --ink:#1d1d1d;
    --dark:#222222;
    --cta:#62b947;
  }
  *{box-sizing:border-box;margin:0;padding:0}
  html,body{width:1200px;height:1200px;overflow:hidden;background:var(--page)}
  body{position:relative;font-family:"Arimo",Arial,sans-serif;color:var(--ink)}

  .flyer{position:absolute;left:20px;top:190px;width:1160px;height:819px;background:var(--paper);box-shadow:0 2px 6px rgba(0,0,0,.25);overflow:hidden}

  .photo{position:absolute}
  .photo--friends{left:0;top:0;width:375px;height:290px;background:linear-gradient(160deg,#f6d7a0 0%,#e7a65c 35%,#8aa7c4 70%,#b86a4a 100%)}
  .photo--coaches{left:375px;top:0;width:399px;height:280px;background:linear-gradient(180deg,#7d6f62 0%,#5d544c 45%,#b9b3ad 100%)}

  .waves{position:absolute;left:0;top:0;width:774px;height:819px}

  .testimonials{position:absolute;left:12px;top:324px;width:352px;font-family:"Roboto Condensed",Arial,sans-serif;font-size:12.6px;line-height:18.2px;text-align:justify}
  .testimonials h2{font-family:"Arimo",Arial,sans-serif;font-size:15.5px;font-weight:700;text-align:center;margin-bottom:6px}
  .testimonials p{margin-bottom:7px}
  .testimonials .client{font-weight:700}

  .intro{position:absolute;left:400px;top:324px;width:350px;text-align:center;font-size:17.2px;line-height:21.5px}
  .intro .services{font-weight:700;font-style:italic}
  .intro .cta-text{margin-top:4px}
  .contact{margin-top:8px}
  .contact .phone{font-size:23px;line-height:30px}
  .contact .phone b{font-weight:700}
  .contact .line{font-size:17.2px;line-height:25px}

  .brand{display:flex;flex-direction:column;align-items:center;position:absolute}
  .brand .mark{border-radius:50%;border:7px solid var(--green)}
  .brand .name{font-family:"Arimo",Arial,sans-serif;font-weight:400;color:var(--brand-blue);text-align:center;line-height:1.15}
  .brand--middle{left:387px;top:608px;width:387px}
  .brand--middle .mark{width:96px;height:96px}
  .brand--middle .name{font-size:22px;margin-top:8px}
  .brand--cover{left:774px;top:42px;width:386px}
  .brand--cover .mark{width:140px;height:140px;border-width:9px}
  .brand--cover .name{font-size:27px;margin-top:10px}

  .offer{position:absolute;left:387px;top:748px;width:387px;height:71px;background:var(--cta);color:#222;text-align:center;font-size:15px;line-height:20px;padding-top:6px}

  .cover{position:absolute;left:774px;top:0;width:386px;height:819px;border-left:1px solid #dddddd}
  .photo--yoga{left:0;top:290px;width:386px;height:400px;background:linear-gradient(180deg,#2f7fd0 0%,#6fb0e6 45%,#86a94f 72%,#5e8c35 100%)}
  .cover-waves{position:absolute;left:0;top:0;width:386px;height:819px}
  .cover-services{position:absolute;left:0;top:708px;width:386px;text-align:center;color:#ffffff;font-size:21.5px;line-height:31px}
</style>
</head>
<body>
  <main class="flyer">
    <div class="photo photo--friends" role="img" aria-label="Photo of a group of happy friends cheering by a car at sunset"></div>
    <div class="photo photo--coaches" role="img" aria-label="Portrait photo of the two coaches"></div>

    <svg class="waves" viewBox="0 0 774 819" aria-hidden="true">
      <path d="M0,205 C180,285 430,285 774,225 L774,819 L0,819 Z" fill="var(--green)"/>
      <path d="M0,240 C190,300 440,290 774,245 L774,819 L0,819 Z" fill="#ffffff"/>
      <path d="M0,255 C200,300 450,285 774,262 L774,819 L0,819 Z" fill="var(--green)"/>
      <path d="M0,278 C200,302 450,277 774,285 L774,819 L0,819 Z" fill="var(--blue)"/>
      <path d="M0,293 C200,305 450,282 774,300 L774,819 L0,819 Z" fill="#ffffff"/>
    </svg>

    <section class="testimonials">
      <h2>Happy Clients Testimonials</h2>
      <p>“I have lost 10 kilos and now have the energy to play with my kids. Thanks Maren for you support/guidance and helping me get rid of my limiting beliefs. I feel I can achieve anything now! The sky’s the limit” - <span class="client">Tessa, Mosman</span></p>
      <p>“I had always wanted to start up own café however every time it came to putting it into practice I would procrastinate and not achieve anything. I became overwhelmed with the whole process and never achieved anything. Maren put it into bite sized chunks and helped me to set small achievable goals. I am now a happy café owner.” - <span class="client">Priya, Double Bay</span></p>
      <p>“Maren has helped to change my life around in all aspects. I would have been lost without her. Thanks Maren for your professionalism, support and guidance.” - <span class="client">Olivia, Cremorne</span></p>
      <p>“I was so busy with kids, work, and my husband I lost who I was. Maren has helped me find the person I am again.” <span class="client">Hannah, Chatswood</span></p>
      <p>“When I started with Coach Maren, I didn’t know anything about coaching. I called her because she helped a friend of mine make a career change that was a perfect fit for her. I had the opportunity to make a change too and did not know where to start. I am now in a job that I love. I would recommend Maren to everyone.” <span class="client">Marcus, Texas America</span></p>
    </section>

    <section class="intro">
      <p>Clearpath Coaching and Meditation Studio is a professional service that can help you achieve the goals that you are looking for in</p>
      <p class="services">Life Coaching, Meditation, and Yoga/Pilates.</p>
      <p class="cta-text">If you are ready to take your life to the next level and would like to know more, please contact us.</p>
      <div class="contact">
        <p class="phone"><b>Phone</b>: 02 9000 4172</p>
        <p class="line">Email:hello@clearpathstudio.com.au</p>
        <p class="line">www.clearpathstudio.com.au</p>
      </div>
    </section>

    <div class="brand brand--middle">
      <span class="mark"></span>
      <span class="name">Clearpath Coaching</span>
    </div>

    <div class="offer">
      <p>Free Introductory Life Coaching</p>
      <p>Phone/Skype session - 20 mins</p>
      <p>(To see if coaching is right for you)</p>
    </div>

    <section class="cover">
      <div class="photo photo--yoga" role="img" aria-label="Photo of women meditating cross-legged on yoga mats on grass by the water"></div>
      <svg class="cover-waves" viewBox="0 0 386 819" aria-hidden="true">
        <path d="M0,232 C130,268 260,268 386,248 L386,262 C260,285 130,282 0,245 Z" fill="var(--blue)"/>
        <path d="M0,245 C130,282 260,285 386,262 L386,318 C260,332 130,330 0,300 Z" fill="var(--green)"/>
        <path d="M0,270 C130,295 260,295 386,283 L386,291 C260,304 130,304 0,282 Z" fill="#ffffff"/>
        <path d="M0,650 C130,630 260,625 386,640 L386,819 L0,819 Z" fill="var(--green)"/>
        <path d="M0,668 C140,655 270,655 386,672 L386,819 L0,819 Z" fill="#ffffff"/>
        <path d="M0,680 C140,668 270,675 386,700 L386,819 L0,819 Z" fill="var(--blue)"/>
        <path d="M0,688 C140,678 270,686 386,712 L386,819 L0,819 Z" fill="var(--dark)"/>
      </svg>
      <div class="cover-services">
        <p>Life Coaching</p>
        <p>Meditation</p>
        <p>Yoga/Pilates.</p>
      </div>
    </section>

    <div class="brand brand--cover">
      <span class="mark"></span>
      <span class="name">Clearpath Coaching</span>
    </div>
  </main>
</body>
</html>
```